Webdesign für Seminaranbieter
Zielgruppe
Die Tessel Academy bietet Kurse, Seminare & Coachings im Bereich der Kommunikation / Persönlichkeitsentwicklung an.
Folgendes Angebot besteht zur Zeit:
Seminare:
- 'Erste Schritte Dialog', eine Einführung in die Kommunikation.
- 'Starke Familien, ruhige Abende' zum Thema Erziehung.
- 'Reife Jahre mit Gelassenheit', zum Thema Älter werden und den Umgang damit.
Kurse:
- 'Gewaltfreie Kommunikation', Übungsgruppe
Coaching:
- Einzelsitzungen mit Hypnose
Ps: im Anhang unter 'Angabot_Vorlage.pdf' finden Sie mehr Infos zu den einezlenen Angebote.
Aufgabenstellung
Bitte berücksichtigen Sie, dass bereits ein Logo besteht (siehe Anhang).
Vom gesamteindruck her sollte die Website aufgeräumt, übersichtlich, harmonisch, freundlich & frisch wirken.
Es wäre super, wenn die Website authentisch wirkt (und weniger '0815 Business Website').
Bitte bedenken Sie, dass die Website sich an Private richtet, die sich nach einem 'strahlenderen & unbeschwerterem Lebene sehnen'.
Wir haben bereits viele Persönlichkeiten stärken können und möchten dies auch witerhin mit viel Herzblut machen.

```html
<!DOCTYPE html>
<html lang="de">
<head>
<meta charset="utf-8">
<title>Tessel Academy – Kommunikation &amp; Persönlichkeitsentwicklung</title>
<link href="https://fonts.googleapis.com/css2?family=Nunito:wght@400;600;700&family=Open+Sans:wght@400;600;700&display=swap" rel="stylesheet">
<style>
  :root {
    --navy: #1d3a5f;
    --text: #2a4160;
    --cyan: #dcf5f9;
    --green: #5cdc84;
    --green-dark: #55d47b;
    --red: #f4505a;
    --white: #ffffff;
    --line: #d4dde6;
    --placeholder: #8fd3e6;
  }
  * { box-sizing: border-box; margin: 0; padding: 0; }
  html, body { width: 1200px; height: 4089px; overflow: hidden; }
  body {
    position: relative;
    background: var(--white);
    font-family: "Open Sans", sans-serif;
    color: var(--text);
  }
  .backdrop { position: absolute; left: 0; top: 0; width: 1200px; height: 4089px; }
  .abs { position: absolute; }

  /* Header */
  .brand {
    left: 122px; top: 40px;
    display: flex; align-items: center; gap: 10px;
    font-family: "Nunito", sans-serif; font-weight: 700;
    font-size: 15px; letter-spacing: 1.5px; color: var(--navy);
  }
  .brand-dot { width: 14px; height: 14px; border-radius: 50%; background: var(--navy); }
  .main-nav {
    left: 474px; top: 47px;
    display: flex; gap: 34px;
    font-family: "Nunito", sans-serif; font-size: 13px; letter-spacing: 1px; color: var(--navy);
  }
  .btn-red {
    background: var(--red); color: var(--white);
    font-family: "Open Sans", sans-serif; font-weight: 700; font-size: 9.5px; letter-spacing: .3px;
    display: flex; align-items: center; justify-content: center; text-transform: uppercase;
  }
  .cta-header { left: 842px; top: 41px; width: 236px; height: 29px; }

  /* Headings */
  .h-hero, .h-section {
    font-family: "Nunito", sans-serif; font-weight: 400; color: var(--navy);
    font-size: 44px; line-height: 58px;
  }
  .lead { font-size: 12.5px; line-height: 21px; color: var(--text); }
  .hero-title { left: 122px; top: 264px; width: 600px; }
  .hero-text { left: 122px; top: 398px; width: 550px; }

  .photo { position: absolute; }

  /* Offer cards */
  .offer-card {
    position: absolute; top: 682px; width: 229px; height: 270px;
    background: var(--white); box-shadow: 0 10px 26px rgba(29,58,95,.12);
    padding: 28px 22px 0;
  }
  .offer-card.is-active { background: linear-gradient(180deg, #63e084, #5ad689); color: var(--white); }
  .offer-icon { width: 26px; height: 38px; }
  .offer-title { font-family: "Nunito", sans-serif; font-weight: 700; font-size: 23px; color: var(--navy); margin-top: 16px; }
  .offer-text { font-size: 12.5px; line-height: 21px; margin-top: 6px; color: var(--text); }
  .offer-link { position: absolute; left: 22px; top: 222px; font-weight: 700; font-size: 12.5px; color: var(--navy); }
  .is-active .offer-title, .is-active .offer-text, .is-active .offer-link { color: var(--white); }
  .is-active .offer-text { opacity: .9; }

  .btn-green {
    position: absolute; width: 235px; height: 46px; border-radius: 3px;
    background: var(--green); color: var(--white);
    font-weight: 700; font-size: 12.5px; letter-spacing: 1px;
    display: flex; align-items: center; justify-content: center;
  }

  /* Newsletter */
  .newsletter-title { left: 284px; top: 2450px; width: 700px; font-family: "Nunito", sans-serif; font-size: 35px; line-height: 44px; color: var(--navy); }
  .newsletter-input {
    left: 284px; top: 2600px; width: 468px; height: 46px;
    border: 1px solid var(--line); background: var(--white);
    font-family: Arial, sans-serif; font-size: 15px; color: var(--placeholder);
    padding: 13px 18px;
  }
  .newsletter-send { left: 775px; top: 2606px; width: 106px; height: 35px; background: var(--green); color: var(--white); font-size: 8px; font-weight: 700; display: flex; align-items: center; justify-content: center; }

  /* Testimonials */
  .avatar { position: absolute; border-radius: 50%; border: 3px solid var(--white); box-shadow: 0 6px 16px rgba(0,0,0,.25); }
  .quote-card {
    left: 365px; top: 2925px; width: 470px; height: 233px;
    background: var(--white); box-shadow: 0 10px 30px rgba(29,58,95,.1);
    padding: 70px 66px 0;
    font-family: "Nunito", sans-serif; font-size: 20px; line-height: 27px; color: var(--navy);
  }

  /* Contact */
  .contact-title { left: 0; top: 3320px; width: 1200px; text-align: center; font-family: "Nunito", sans-serif; font-weight: 600; font-size: 31px; color: var(--navy); }
  .contact-intro { left: 0; top: 3378px; width: 1200px; text-align: center; font-family: "Nunito", sans-serif; font-size: 17.5px; line-height: 23px; color: var(--navy); }
  .contact-intro strong { font-weight: 700; }
  .field-label { position: absolute; font-size: 8px; font-weight: 700; color: var(--navy); text-transform: uppercase; }
  .field {
    position: absolute; width: 286px; height: 41px;
    background: var(--white); border: 1px solid var(--line);
    font-size: 11px; color: var(--text); padding: 13px 14px;
  }
  .field-area { width: 607px; height: 119px; line-height: 17px; padding: 13px 16px; font-size: 10.5px; }
  .consent { left: 287px; top: 3808px; display: flex; align-items: center; gap: 12px; font-size: 11px; color: var(--text); }
  .checkbox { width: 18px; height: 18px; border: 1px solid #9fc9dc; background: var(--white); border-radius: 2px; }
  .cta-form { left: 284px; top: 3852px; width: 237px; height: 30px; }

  /* Footer */
  .footer-rule { left: 122px; top: 3952px; width: 956px; height: 2px; background: var(--navy); }
  .footer-links { right: 122px; top: 3995px; display: flex; gap: 28px; font-weight: 600; font-size: 15px; color: var(--navy); letter-spacing: .3px; }
</style>
</head>
<body>

<svg class="backdrop" viewBox="0 0 1200 4089" aria-hidden="true">
  <path fill="var(--cyan)" d="M0 0 H1200 V1270 C1120 1120 1020 1030 900 1035 C760 1040 640 1000 500 960 C330 905 180 880 110 720 C70 620 0 560 0 420 Z"/>
  <path fill="var(--cyan)" d="M0 2730 C150 2850 300 2910 500 2925 C620 2935 700 2990 725 3100 C750 3200 860 3265 1000 3272 C1100 3276 1160 3270 1200 3262 V4089 H0 Z"/>
</svg>

<header>
  <div class="abs brand"><span class="brand-dot"></span>TESSEL ACADEMY</div>
  <nav class="abs main-nav">
    <span>HOME</span><span>ANGEBOT</span><span>KONTAKT</span><span>ÜBER UNS</span>
  </nav>
  <div class="abs btn-red cta-header">Kostenlose Erstberatung anfordern</div>
</header>

<section class="hero">
  <h1 class="abs h-hero hero-title">Kommunikation &amp;<br>Persönlichkeitsentwicklung</h1>
  <p class="abs lead hero-text">Lorem ipsum dolor sit amet, consetetur sadipscing elitr, sed diam nonumy eirmod tempor invidunt ut labore et dolore magna aliquyam erat, sed diam voluptua.</p>
  <svg class="photo" style="left:712px;top:160px" width="395" height="400" viewBox="0 0 395 400" role="img" aria-label="Porträtfoto einer lächelnden Frau mit dunklen Haaren">
    <defs><linearGradient id="gHero" x1="0" y1="0" x2="1" y2="1"><stop offset="0" stop-color="#c9b8a6"/><stop offset=".5" stop-color="#8a6a5a"/><stop offset="1" stop-color="#3b2a28"/></linearGradient></defs>
    <path fill="url(#gHero)" d="M150 2 C230 -8 300 70 360 160 C410 230 390 270 330 320 C260 380 160 410 100 390 C30 365 4 300 2 200 C0 110 60 14 150 2 Z"/>
  </svg>
</section>

<section class="offers">
  <article class="offer-card is-active" style="left:122px">
    <svg class="offer-icon" viewBox="0 0 26 38" fill="none" stroke="currentColor" stroke-width="2.4" stroke-linejoin="round"><path d="M13 2 L3 35 L13 27 L23 35 Z M8 22 H18"/></svg>
    <h2 class="offer-title">Starter Kit</h2>
    <p class="offer-text">Lorem ipsum dolor sit amet, consetetur sadipscing elitr, sed diam</p>
    <span class="offer-link">Mehr erfahren</span>
  </article>
  <article class="offer-card" style="left:363px">
    <svg class="offer-icon" viewBox="0 0 26 38" fill="none" stroke="var(--navy)" stroke-width="2.4" stroke-linejoin="round"><path d="M13 2 L3 35 L13 27 L23 35 Z M8 22 H18"/></svg>
    <h2 class="offer-title">Kind &amp; Eltern</h2>
    <p class="offer-text">Lorem ipsum dolor sit amet, consetetur sadipscing elitr, sed diam</p>
    <span class="offer-link">Mehr erfahren</span>
  </article>
  <article class="offer-card" style="left:607px">
    <svg class="offer-icon" viewBox="0 0 26 38" fill="none" stroke="var(--navy)" stroke-width="2.4" stroke-linejoin="round"><path d="M13 2 L3 35 L13 27 L23 35 Z M8 22 H18"/></svg>
    <h2 class="offer-title">Realität</h2>
    <p class="offer-text">Lorem ipsum dolor sit amet, consetetur sadipscing elitr, sed diam</p>
    <span class="offer-link">Mehr erfahren</span>
  </article>
  <article class="offer-card" style="left:850px">
    <svg class="offer-icon" viewBox="0 0 26 38" fill="none" stroke="var(--navy)" stroke-width="2.4" stroke-linejoin="round"><path d="M13 2 L3 35 L13 27 L23 35 Z M8 22 H18"/></svg>
    <h2 class="offer-title">Hypnose</h2>
    <p class="offer-text">Lorem ipsum dolor sit amet, consetetur sadipscing elitr, sed diam</p>
    <span class="offer-link">Mehr erfahren</span>
  </article>
</section>

<section class="next-step">
  <h2 class="abs h-section" style="left:122px;top:1110px;width:560px">Bereit für den nächsten<br>Schritt?</h2>
  <p class="abs lead" style="left:122px;top:1242px;width:480px">Lorem ipsum dolor sit amet, consetetur sadipscing elitr, sed diam nonumy eirmod tempor invidunt ut labore et dolore magna aliquyam erat, sed diam voluptua. At vero eos et accusam et justo duo dolores et ea rebum. Stet clita kasd gubergren, no sea takimata sanctus est Lorem</p>
  <div class="btn-green" style="left:122px;top:1384px">KONTAKTIEREN</div>
  <svg class="photo" style="left:738px;top:1166px" width="245" height="242" viewBox="0 0 245 242" role="img" aria-label="Schwarzweißfoto eines Jungen, der in ein Mikrofon ruft">
    <defs><linearGradient id="gShout" x1="0" y1="0" x2="1" y2="1"><stop offset="0" stop-color="#d8d8d8"/><stop offset=".6" stop-color="#9a9a9a"/><stop offset="1" stop-color="#5e5e5e"/></linearGradient></defs>
    <path fill="url(#gShout)" d="M70 2 C140 -6 200 60 235 110 C255 140 230 170 180 200 C130 232 80 250 40 230 C8 214 0 170 2 110 C4 50 20 8 70 2 Z"/>
  </svg>
</section>

<section class="community">
  <h2 class="abs h-section" style="left:122px;top:1804px;width:480px">Lorem ipsum dolor sit amet, consetetur</h2>
  <p class="abs lead" style="left:122px;top:1952px;width:480px">Lorem ipsum dolor sit amet, consetetur sadipscing elitr, sed diam nonumy eirmod tempor invidunt ut labore et dolore magna aliquyam erat, sed diam voluptua. At vero eos et accusam et justo duo dolores et ea rebum. Stet clita kasd gubergren, no sea takimata sanctus est Lorem ipsum dolor sit amet. Lorem ipsum dolor sit amet,</p>
  <div class="btn-green" style="left:122px;top:2111px">KONTAKTIEREN</div>
  <svg class="photo" style="left:603px;top:1571px" width="597" height="826" viewBox="0 0 597 826" role="img" aria-label="Foto vieler übereinandergelegter Hände in einer Gruppe">
    <defs><radialGradient id="gHands" cx=".55" cy=".45" r=".7"><stop offset="0" stop-color="#a8785e"/><stop offset=".5" stop-color="#4a3a3a"/><stop offset="1" stop-color="#1b2233"/></radialGradient></defs>
    <path fill="url(#gHands)" d="M480 2 C540 -4 580 4 597 12 V826 C520 810 440 760 360 680 C260 580 130 470 40 360 C-10 300 -2 230 60 180 C150 110 280 110 350 80 C410 50 430 8 480 2 Z"/>
  </svg>
</section>

<section class="newsletter">
  <h2 class="abs newsletter-title">Melde dich für den Newsletter an und bleibe immer auf den aktuellsten Stand</h2>
  <div class="abs newsletter-input">Email Adresse eingeben</div>
  <div class="abs newsletter-send">SEND</div>
</section>

<section class="testimonials">
  <div class="avatar" role="img" aria-label="Porträt einer jungen Frau" style="left:163px;top:2800px;width:107px;height:107px;background:radial-gradient(circle,#8a6a5e,#2e2a2a)"></div>
  <div class="avatar" role="img" aria-label="Porträt einer lachenden Frau" style="left:996px;top:2800px;width:124px;height:124px;background:radial-gradient(circle,#a99685,#4d5a46)"></div>
  <div class="avatar" role="img" aria-label="Porträt eines Mannes" style="left:957px;top:3013px;width:53px;height:53px;background:radial-gradient(circle,#7a6a60,#2a2a2c)"></div>
  <div class="avatar" role="img" aria-label="Porträt einer Frau mit Jeansjacke" style="left:122px;top:3087px;width:118px;height:118px;background:radial-gradient(circle,#8a97a8,#3d4a60)"></div>
  <div class="abs quote-card">Lorem ipsum dolor sit amet, consetetur sadipscing elitr, sed diam nonumy eirmod tempor invidunt ut labore et dolore magna</div>
  <div class="avatar" role="img" aria-label="Porträt einer blonden Frau" style="left:545px;top:2862px;width:110px;height:110px;background:radial-gradient(circle,#c9a28a,#6a4a3e)"></div>
</section>

<section class="contact">
  <h2 class="abs contact-title">Worauf warten Sie?</h2>
  <p class="abs contact-intro">Kontaktieren Sie uns jetzt für ein <strong>kostenloses Beratungsgespräch</strong> und<br>lassen Sie uns Ihre Herausforderungen lösen.<br>Wir melden uns innerhalb der nächsten 24 Stunden!</p>

  <span class="field-label" style="left:287px;top:3496px">Name*</span>
  <div class="field" style="left:287px;top:3511px">Lena Beispiel</div>
  <span class="field-label" style="left:608px;top:3496px">Herausforderung*</span>
  <div class="field" style="left:608px;top:3511px">Kommnikation</div>

  <span class="field-label" style="left:287px;top:3570px">Email*</span>
  <div class="field" style="left:287px;top:3585px">lena.beispiel@post-beispiel.de</div>
  <span class="field-label" style="left:608px;top:3570px">Telefonnummer*</span>
  <div class="field" style="left:608px;top:3585px">+49 | 40 55 61 72 18</div>

  <span class="field-label" style="left:287px;top:3659px">Anliegen*</span>
  <div class="field field-area" style="left:287px;top:3674px">Lorem ipsum dolor sit amet, consetetur sadipscing elitr, sed diam nonumy eirmod tempor invidunt ut labore et dolore magna aliquyam erat, sed diam voluptua. At vero eos et accusam et justo duo do.</div>

  <div class="abs consent"><span class="checkbox"></span>Datenschutzerklärung gelesen und akzeptiert.*</div>
  <div class="abs btn-red cta-form">Kostenlose Erstberatung anfordern</div>
</section>

<footer>
  <div class="abs footer-rule"></div>
  <nav class="abs footer-links"><span>DATENSCHUTZERKLÄRUNG</span><span>AGB</span></nav>
</footer>

</body>
</html>
```